Business card for different employees

A professional new updated design incorporating our current business's color themes and styles such as our on-site service trucks decals included in pictures attached. Our current business card is very simple and not professionally designed. We are a small family business but want a professional corporate look.

Target Market(s)

Cards to be handed out to new customers , corperate meetings. For our on site service operators.

Industry/Entity Type

Hydraulic

Contact Information for Business Card

Address, website, phone number, email, logo.
slogan - "Industry chosen hose and fittings provider".
24/7 on-site service , supply and hose management
Experienced , indpendant , family owned

Font styles to use
Sans Serif

Requirements
Must have
• Easily editable so that I can add different names and different roles for employees etc.
Nice to have
• Freedom with colour doesn't necessarily have to be blue but that is our company colour theme with trucks and logo so makes sense for the card to have blue like the trucks.

```html
<!DOCTYPE html>
<html lang="en">
<head>
<meta charset="utf-8">
<title>Keystone Hose &amp; Fittings – Business Card</title>
<link href="https://fonts.googleapis.com/css2?family=Exo+2:wght@700&family=Roboto:wght@400&display=swap" rel="stylesheet">
<style>
  :root {
    --backdrop: #878787;
    --card-white: #ffffff;
    --card-black: #1a1a19;
    --brand-blue: #1a2fc4;
    --ink: #1e1e1e;
    --paper-text: #ffffff;
  }
  * { margin: 0; padding: 0; box-sizing: border-box; }
  html, body { width: 1065px; height: 1200px; overflow: hidden; }
  body {
    background: var(--backdrop);
    position: relative;
    font-family: "Roboto", Arial, sans-serif;
  }

  .card { position: absolute; }

  /* Front */
  .card--front {
    left: 292px; top: 218px;
    width: 583px; height: 363px;
    background: var(--card-white);
    border-radius: 0 182px 182px 0 / 0 182px 182px 0;
    box-shadow: 2px 3px 3px rgba(0,0,0,0.55);
  }
  .front-brand {
    position: absolute;
    left: 66px; top: 45px;
    width: 58px; height: 272px;
  }
  .front-brand__name {
    position: absolute;
    left: 29px; top: 96px;
    transform: translate(-50%, -50%) rotate(-90deg);
    white-space: nowrap;
    font-family: "Exo 2", Arial, sans-serif;
    font-weight: 700;
    font-size: 15px;
    letter-spacing: 1px;
    color: var(--brand-blue);
  }
  .front-brand__mark {
    position: absolute;
    left: 8px; bottom: 8px;
    width: 42px; height: 42px;
    border-radius: 50%;
    background: var(--brand-blue);
  }

  .details {
    position: absolute;
    left: 176px; top: 93px;
    color: var(--ink);
  }
  .details__name {
    font-family: "Exo 2", Arial, sans-serif;
    font-weight: 700;
    font-size: 21px;
    line-height: 24px;
    color: var(--brand-blue);
  }
  .details__role {
    font-size: 17.5px;
    line-height: 20px;
  }
  .contact-list {
    list-style: none;
    margin-top: 12px;
  }
  .contact-list li {
    display: flex; align-items: center;
    font-size: 17.5px;
    line-height: 22.5px;
  }
  .contact-list svg {
    width: 18px; height: 18px;
    margin-right: 5px;
    flex: none;
  }
  .address {
    margin-top: 10px;
    font-size: 17.5px;
    line-height: 21px;
    font-style: normal;
  }

  /* Back */
  .card--back {
    left: 263px; top: 623px;
    width: 583px; height: 364px;
    background: var(--card-black);
    border-radius: 182px 0 0 182px / 182px 0 0 182px;
    box-shadow: 2px 3px 3px rgba(0,0,0,0.55);
  }
  .back-brand {
    position: absolute;
    left: 89px; top: 138px;
    display: flex; align-items: center;
  }
  .back-brand__mark {
    width: 86px; height: 86px;
    border-radius: 50%;
    background: var(--brand-blue);
    margin-right: 18px;
    flex: none;
  }
  .back-brand__name {
    font-family: "Exo 2", Arial, sans-serif;
    font-weight: 700;
    font-size: 27px;
    line-height: 31px;
    letter-spacing: 1px;
    color: var(--paper-text);
  }
  .tagline {
    position: absolute;
    left: 0; right: 0; top: 248px;
    text-align: center;
    font-size: 17.5px;
    line-height: 21px;
    color: var(--paper-text);
  }
</style>
</head>
<body>

  <section class="card card--front">
    <div class="front-brand">
      <span class="front-brand__name">KEYSTONE HOSE &amp; FITTINGS</span>
      <span class="front-brand__mark"></span>
    </div>

    <div class="details">
      <h1 class="details__name">DANIEL MORRIS</h1>
      <p class="details__role">Managing Director</p>

      <ul class="contact-list">
        <li>
          <svg viewBox="0 0 24 24" fill="none" stroke="var(--brand-blue)" stroke-width="2.2" stroke-linecap="round" stroke-linejoin="round">
            <path d="M5 3h4l2 5-2.5 1.5a11 11 0 0 0 6 6L16 13l5 2v4a2 2 0 0 1-2 2A16 16 0 0 1 3 5a2 2 0 0 1 2-2z"/>
            <path d="M15 3a6 6 0 0 1 6 6M15 7a2 2 0 0 1 2 2"/>
          </svg>
          0400 123 456
        </li>
        <li>
          <svg viewBox="0 0 24 24">
            <rect x="1" y="5" width="22" height="14" fill="var(--brand-blue)"/>
            <path d="M1 5l11 8 11-8M1 19l8-7M23 19l-8-7" fill="none" stroke="#fff" stroke-width="1.5"/>
          </svg>
          info@keystonehose.com
        </li>
        <li>
          <svg viewBox="0 0 24 24" fill="none" stroke="var(--brand-blue)" stroke-width="1.8">
            <circle cx="12" cy="12" r="10"/>
            <ellipse cx="12" cy="12" rx="4.5" ry="10"/>
            <path d="M2 12h20M4 7h16M4 17h16"/>
          </svg>
          www.keystonehose.com.au
        </li>
      </ul>

      <address class="address">
        421, Address line here<br>
        Country Name, 45452
      </address>
    </div>
  </section>

  <section class="card card--back">
    <div class="back-brand">
      <span class="back-brand__mark"></span>
      <p class="back-brand__name">KEYSTONE<br>HOSE &amp; FITTINGS</p>
    </div>
    <p class="tagline">
      24/7 On-site Service &nbsp;|&nbsp; Supply and Hose Management<br>
      Experienced, Indpendant, Family Owned
    </p>
  </section>

</body>
</html>
```